Flyer "We are moving"

Hi i need a Flyer for moving our Surfshop:

- When we move: 11.March 2020
- Old Adress: Lindenweg 12, 8004 Zürich
- New Adress: Lindenweg 48. 8004 Zürich

Please create something great, it may be simple but with a certain irony.

If you have any questions, please write to me

```html
<!DOCTYPE html>
<html lang="de">
<head>
<meta charset="utf-8">
<title>We Are Moving – Waveline Surfshop</title>
<link rel="stylesheet" href="https://fonts.googleapis.com/css2?family=Open+Sans:wght@400;600;700;800&display=swap">
<style>
  :root {
    --backdrop: #e9e9e9;
    --ink: #111111;
    --orange: #e88d2a;
    --white: #ffffff;
    --navy: #2f4256;
    --logo-ink: #1d1d1d;
  }
  * { box-sizing: border-box; margin: 0; padding: 0; }
  html, body {
    width: 1200px;
    height: 800px;
    overflow: hidden;
    background: var(--backdrop);
    font-family: "Open Sans", Arial, sans-serif;
  }
  .flyer {
    position: absolute;
    left: 340px;
    top: 40px;
    width: 520px;
    height: 720px;
    background: var(--ink);
    overflow: hidden;
    color: var(--white);
  }
  .flyer-backdrop {
    position: absolute;
    inset: 0;
  }
  .brand {
    position: absolute;
    left: 26px;
    top: 18px;
    color: var(--logo-ink);
  }
  .brand-name {
    font-weight: 800;
    font-size: 30px;
    line-height: 30px;
    letter-spacing: -0.5px;
  }
  .brand-tagline {
    font-weight: 600;
    font-size: 11px;
    letter-spacing: 2px;
    margin-top: 4px;
  }
  .badge-new {
    position: absolute;
    right: 26px;
    top: 16px;
    text-align: center;
    color: var(--ink);
    font-weight: 700;
    line-height: 16px;
  }
  .badge-new .badge-big { font-size: 16px; }
  .badge-new .badge-small { font-size: 12px; }
  .map-illustration {
    position: absolute;
    left: 128px;
    top: 82px;
    width: 204px;
    height: 204px;
    border-radius: 50%;
    background: radial-gradient(circle at 50% 55%, #4a8f6a 0%, #3a6a5a 35%, var(--navy) 70%);
    border: 4px solid var(--white);
  }
  .headline {
    position: absolute;
    left: 0;
    width: 460px;
    top: 300px;
    text-align: center;
    font-weight: 700;
    font-size: 52px;
    line-height: 62px;
    letter-spacing: 1px;
  }
  .headline-rule {
    position: absolute;
    left: 78px;
    top: 432px;
    width: 304px;
    height: 3px;
    background: var(--white);
  }
  .move-date {
    position: absolute;
    left: 0;
    width: 460px;
    top: 446px;
    text-align: center;
    font-weight: 700;
    font-size: 26px;
  }
  .move-date .month { color: var(--orange); }
  .address {
    position: absolute;
    top: 505px;
    font-weight: 700;
  }
  .address-old { left: 28px; text-align: left; }
  .address-new { right: 28px; text-align: right; }
  .address-label {
    font-weight: 600;
    font-size: 26px;
    padding-bottom: 4px;
    border-bottom: 2px solid var(--white);
    display: inline-block;
    margin-bottom: 12px;
  }
  .address-new .address-label { margin-top: 12px; }
  .address-line {
    font-size: 21px;
    line-height: 30px;
  }
  .website {
    position: absolute;
    left: 0;
    width: 100%;
    top: 662px;
    text-align: center;
    color: var(--orange);
    font-weight: 600;
    font-size: 14px;
    letter-spacing: 0.5px;
  }
</style>
</head>
<body>
  <main class="flyer">
    <svg class="flyer-backdrop" width="520" height="720" viewBox="0 0 520 720" aria-hidden="true">
      <polygon points="0,0 520,0 520,100 0,250" fill="#e88d2a"/>
      <polygon points="0,256 520,106 520,112 0,262" fill="#ffffff"/>
    </svg>

    <header class="brand">
      <div class="brand-name">WAVELINE<br>SURFSHOP</div>
      <div class="brand-tagline">RIDE WITH US</div>
    </header>

    <div class="badge-new">
      <div class="badge-big">NEW</div>
      <div class="badge-small">LOCATION</div>
    </div>

    <div class="map-illustration" role="img" aria-label="Illustration of a folded map with a red location pin inside a dark navy circle"></div>

    <h1 class="headline">WE ARE<br>MOVING</h1>
    <div class="headline-rule"></div>
    <p class="move-date">11.<span class="month">March</span> 2020</p>

    <section class="address address-old">
      <h2 class="address-label">Old Address</h2>
      <p class="address-line">Lindenweg 12,<br>8004 Zürich</p>
    </section>

    <section class="address address-new">
      <h2 class="address-label">New Address</h2>
      <p class="address-line">Lindenweg<br>48. 8004 Zürich</p>
    </section>

    <p class="website">WWW.WAVELINE-SURF.CH</p>
  </main>
</body>
</html>
```